Company Brochure promoting our Managed Services Business (MSP)

Objective: Is the brochure meant to generate leads, educate potential clients, and promote our Managed Services Business.
Target Audience: is for Small to medium size business.
A managed service provider like Brivanta Advisory Group handles a variety of different responsibilities for Business
. We oversee vital IT resources such as:
Email
Cloud integration
Data storage
Networking
Cybersecurity
File backup
Help desk services
Our firm also provides remote monitoring services and updates. As part of our managed service provider solutions, we will continually report on the performance and quality of your network. We can even help your organization acquire new hardware and software.
At Brivanta Advisory Group we specialize in empowering commercial businesses with robust IT solutions tailored to enhance efficiency, security, and scalability. With years of expertise in Managed Services, we understand the unique challenges businesses face in today’s digital landscape.
Call-to-Action (CTA):
Encourage readers to contact you, visit your website, or schedule a consultation.
you can get an overview of BAG at www..brivantaag.com.
Layout: Opt for a clean, easy-to-read layout with well-defined sections.
Imagery:
Include professional photos, custom graphics, or icons that represent your services.
Avoid generic stock images when possible.
Format: Tri-fold, bi-fold, depending on the amount of information.
We would like to have a section of the "q7" from our web site.
I have attached the Logos.
Target Market(s)
Small to Medium Business
Look and feel

```html
<!DOCTYPE html>
<html lang="en">
<head>
<meta charset="utf-8">
<title>Brivanta Advisory Group – Managed Services Brochure</title>
<link rel="stylesheet" href="https://fonts.googleapis.com/css2?family=Jost:wght@400;500&family=Montserrat:wght@700;800&display=swap">
<style>
:root{
  --bg:#b3b3b3;
  --bg-dark:#6a6a6a;
  --teal:#1a5063;
  --teal-strip:#1d5d70;
  --navy:#14354c;
  --navy-deep:#10304a;
  --ink:#123049;
  --white:#ffffff;
  --text:#1d2a36;
}
*{box-sizing:border-box;margin:0;padding:0}
html,body{width:1200px;height:2695px;overflow:hidden}
body{background:linear-gradient(180deg,var(--bg) 0,var(--bg) 1760px,var(--bg-dark) 1760px,var(--bg-dark) 100%);font-family:"Jost",sans-serif;position:relative}
.spread{position:absolute;left:92px;width:1015px;height:718px;box-shadow:0 2px 8px rgba(0,0,0,.25);overflow:hidden}
.spread--outer{top:931px}
.spread--inner{top:1868px;background:var(--white)}
.panel{position:absolute;top:0;height:100%;width:508px}
.panel--left{left:0}
.panel--right{left:507px}

/* outer spread */
.back{background:linear-gradient(180deg,#1b5064 0%,#195669 55%,#1b5468 100%)}
.cta-box{position:absolute;left:84px;top:247px;width:343px;height:136px;border:2px solid var(--white);color:var(--white);font-size:22px;line-height:27px;text-align:center;padding:26px 0 0;white-space:nowrap}
.cta-pointer{position:absolute;left:222px;top:383px}
.cta-url{position:absolute;left:0;width:100%;top:446px;padding-right:20px;text-align:center;color:var(--white);font-family:"Montserrat",sans-serif;font-weight:700;font-size:33px}
.cover{background:var(--navy)}
.cover-photo{position:absolute;left:0;top:150px;width:508px;height:400px;background:radial-gradient(ellipse 180px 130px at 45% 55%,rgba(215,200,220,.75),rgba(80,110,150,.35) 60%,rgba(20,53,76,0) 100%)}
.brand{position:absolute;display:flex;align-items:center;gap:12px;color:var(--white);font-family:"Jost",sans-serif;font-weight:500}
.brand--cover{left:128px;top:56px;font-size:22px;line-height:25px}
.brand-mark{width:76px;height:76px;border:2px solid var(--white);flex:none}
.cover-title{position:absolute;left:0;width:100%;top:565px;text-align:center;color:var(--white);font-family:"Montserrat",sans-serif;font-weight:800;font-size:21px;line-height:27px}
.cover-sub{position:absolute;left:0;width:100%;top:630px;text-align:center;color:var(--white);font-size:19px;line-height:26px}

/* inner left */
.services{background:var(--navy)}
.services-strip{position:absolute;left:0;top:0;width:50px;height:718px;background:var(--teal-strip)}
.services-rail{position:absolute;left:50px;top:0;width:6px;height:718px;background:var(--white)}
.services-body{position:absolute;left:56px;top:0;width:452px;height:534px;background:var(--navy)}
.services-title{position:absolute;left:76px;top:36px;width:400px;display:flex;align-items:center;gap:18px;color:var(--white);font-size:30px;font-weight:400}
.services-title::before,.services-title::after{content:"";flex:1;height:1px;background:rgba(255,255,255,.5)}
.service{position:absolute;left:18px;display:flex;align-items:center}
.service-icon{width:64px;height:64px;border-radius:50%;background:var(--navy);border:3px solid var(--white);display:flex;align-items:center;justify-content:center;position:relative;z-index:2}
.service-label{background:var(--white);color:var(--ink);font-family:"Montserrat",sans-serif;font-weight:800;font-size:21px;height:44px;line-height:44px;padding:0 10px 0 12px;margin-left:10px}
.services-foot{position:absolute;left:56px;top:534px;width:452px;height:184px;background:var(--white);padding:20px 16px 0 12px;color:var(--text);font-size:11.5px;line-height:15px}
.services-foot p+p{margin-top:14px}

/* inner right */
.method{position:absolute;left:0;top:0;width:508px;height:285px;background:var(--white)}
.method-mark{position:absolute;left:28px;top:92px;display:flex;align-items:center;gap:14px}
.method-dot{width:64px;height:64px;border-radius:50%;background:var(--navy);flex:none}
.method-name{font-family:"Montserrat",sans-serif;font-weight:800;color:var(--ink);font-size:48px;line-height:1}
.method-title{position:absolute;left:236px;top:44px;font-family:"Montserrat",sans-serif;font-weight:800;color:var(--ink);font-size:29px}
.method-text{position:absolute;left:236px;top:94px;width:222px;font-size:11.5px;line-height:15px;color:var(--text)}
.method-text b{font-weight:500}
.vision{position:absolute;left:0;top:285px;width:508px;height:249px;background:linear-gradient(90deg,#163e56 0%,#1b5468 60%,#1d5d72 100%)}
.vision-photo{position:absolute;right:0;top:0;width:240px;height:249px;background:radial-gradient(ellipse 120px 110px at 60% 55%,rgba(170,215,230,.55),rgba(29,93,114,0) 80%)}
.vision-tab{position:absolute;left:30px;top:-18px;background:var(--navy-deep);color:var(--white);font-family:"Montserrat",sans-serif;font-weight:800;font-size:21px;height:42px;line-height:42px;padding:0 18px}
.vision-text{position:absolute;left:32px;top:42px;width:238px;color:var(--white);font-size:11.5px;line-height:15px}
.resources{position:absolute;left:0;top:534px;width:508px;height:184px;background:var(--white)}
.resources-photo{position:absolute;right:0;top:0;width:220px;height:184px;background:linear-gradient(90deg,rgba(255,255,255,1) 0%,rgba(214,226,236,.8) 45%,rgba(150,175,200,.9) 100%)}
.resources-title{position:absolute;left:29px;top:12px;font-family:"Montserrat",sans-serif;font-weight:800;font-size:16px;color:var(--ink)}
.resources-list{position:absolute;left:29px;top:44px;list-style:none;display:grid;grid-template-columns:140px 140px;grid-auto-flow:column;grid-template-rows:repeat(4,18.5px);font-size:12px;color:var(--text)}
.resources-list li{display:flex;align-items:center;gap:8px}
</style>
</head>
<body>

<section class="spread spread--outer">
  <div class="panel panel--left back">
    <div class="cta-box">Encourage readers to contact<br>you, visit your website, or<br>schedule a consultation.</div>
    <svg class="cta-pointer" width="44" height="22" viewBox="0 0 44 22"><polygon points="0,0 44,0 22,22" fill="#fff"/></svg>
    <div class="cta-url">brivantaag.com</div>
  </div>
  <div class="panel panel--right cover">
    <div class="cover-photo" role="img" aria-label="Photo of a hand touching a glowing digital interface"></div>
    <div class="brand brand--cover"><span class="brand-mark"></span><span>BRIVANTA<br>ADVISORY<br>GROUP</span></div>
    <h1 class="cover-title">PROVIDING INNOVATIVE<br>TECHNOLOGY SOLUTIONS</h1>
    <p class="cover-sub">Brivanta can help guide you through to<br>your destination.</p>
  </div>
</section>

<section class="spread spread--inner">
  <div class="panel panel--left services">
    <div class="services-strip"></div>
    <div class="services-body"></div>
    <div class="services-rail"></div>
    <h2 class="services-title">Our Services</h2>

    <div class="service" style="top:91px">
      <div class="service-icon"><svg width="30" height="24" viewBox="0 0 30 24" fill="#fff"><circle cx="10" cy="13" r="7"/><circle cx="10" cy="13" r="3" fill="#14354c"/><circle cx="23" cy="7" r="5"/><circle cx="23" cy="7" r="2" fill="#14354c"/><circle cx="23" cy="19" r="4"/><circle cx="23" cy="19" r="1.6" fill="#14354c"/></svg></div>
      <div class="service-label">Workflow Mangment</div>
    </div>
    <div class="service" style="top:180px">
      <div class="service-icon"><svg width="28" height="24" viewBox="0 0 28 24" fill="none" stroke="#fff" stroke-width="2"><rect x="10" y="1" width="8" height="6"/><rect x="2" y="16" width="8" height="6"/><rect x="18" y="16" width="8" height="6"/><path d="M14 7v5M6 16v-4h16v4"/></svg></div>
      <div class="service-label">Account Mangament Services</div>
    </div>
    <div class="service" style="top:268px">
      <div class="service-icon"><svg width="26" height="26" viewBox="0 0 26 26" fill="#fff"><path d="M6 3l4 0 2 6-3 2c1 3 3 5 6 6l2-3 6 2 0 4c0 2-2 3-4 3C10 23 3 16 3 7c0-2 1-4 3-4z"/><path d="M16 4a6 6 0 0 1 6 6M16 8a2 2 0 0 1 2 2" stroke="#fff" stroke-width="1.6" fill="none"/></svg></div>
      <div class="service-label">Business Technologies</div>
    </div>
    <div class="service" style="top:356px">
      <div class="service-icon"><svg width="26" height="28" viewBox="0 0 26 28" fill="#fff"><polygon points="13,1 25,6 13,11 1,6"/><circle cx="13" cy="14" r="5"/><path d="M3 27c0-6 4-8 10-8s10 2 10 8z"/></svg></div>
      <div class="service-label">Training &amp; education Services</div>
    </div>
    <div class="service" style="top:456px">
      <div class="service-icon"><svg width="30" height="24" viewBox="0 0 30 24" fill="none" stroke="#fff" stroke-width="2"><rect x="5" y="3" width="20" height="14"/><path d="M1 20h28"/></svg></div>
      <div class="service-label">Managed Services</div>
    </div>

    <div class="services-foot">
      <p>Our firm also provides remote monitoring services and updates. As part of our managed service provider solutions, we will continually report on the performance and quality of your network. We can even help your organization acquire new hardware and software.</p>
      <p>At Brivanta Advisory Group we specialize in empowering commercial businesses with robust IT solutions tailored to enhance efficiency, security, and scalability. With years of expertise in Managed Services, we understand the unique challenges businesses face in today’s digital landscape.</p>
    </div>
  </div>

  <div class="panel panel--right">
    <div class="method">
      <div class="method-mark"><span class="method-dot"></span><span class="method-name">q7</span></div>
      <h2 class="method-title">Methodology</h2>
      <p class="method-text">Brivanta Advisory Group believes every successful technology initiative requires a structured, results-driven approach. Our q7 methodology <b>Evaluate, Enhance, Engineer, Execute, and Evolve</b> is designed to ensure each project not only meets your immediate needs but also positions your organization for long-term success.</p>
    </div>

    <div class="vision">
      <div class="vision-photo" role="img" aria-label="Photo of glowing light bulbs on a blue background"></div>
      <h2 class="vision-tab">OUR VISION</h2>
      <p class="vision-text">Brivanta Advisory Group empowers your business to thrive in the digital age. Our team of expert consultants specializes in transforming your technology landscape – streamlining operations, enhancing security, and driving innovation. Whether you’re looking to implement cutting-edge solutions or optimize existing systems, we tailor our approach to meet your unique needs, ensuring you stay ahead of the competition and achieve your strategic goals</p>
    </div>

    <div class="resources">
      <div class="resources-photo" role="img" aria-label="Photo of a laptop with a security shield overlay"></div>
      <h3 class="resources-title">We oversee vital IT resources such as:</h3>
      <ul class="resources-list">
        <li><svg width="14" height="14" viewBox="0 0 14 14" fill="none" stroke="#123049" stroke-width="1.6"><rect x="1" y="3" width="10" height="10"/><path d="M3 7l3 3 7-9"/></svg>Email</li>
        <li><svg width="14" height="14" viewBox="0 0 14 14" fill="none" stroke="#123049" stroke-width="1.6"><rect x="1" y="3" width="10" height="10"/><path d="M3 7l3 3 7-9"/></svg>Cloud integration</li>
        <li><svg width="14" height="14" viewBox="0 0 14 14" fill="none" stroke="#123049" stroke-width="1.6"><rect x="1" y="3" width="10" height="10"/><path d="M3 7l3 3 7-9"/></svg>Data storage</li>
        <li><svg width="14" height="14" viewBox="0 0 14 14" fill="none" stroke="#123049" stroke-width="1.6"><rect x="1" y="3" width="10" height="10"/><path d="M3 7l3 3 7-9"/></svg>Networking</li>
        <li><svg width="14" height="14" viewBox="0 0 14 14" fill="none" stroke="#123049" stroke-width="1.6"><rect x="1" y="3" width="10" height="10"/><path d="M3 7l3 3 7-9"/></svg>Cybersecurity</li>
        <li><svg width="14" height="14" viewBox="0 0 14 14" fill="none" stroke="#123049" stroke-width="1.6"><rect x="1" y="3" width="10" height="10"/><path d="M3 7l3 3 7-9"/></svg>File backup</li>
        <li><svg width="14" height="14" viewBox="0 0 14 14" fill="none" stroke="#123049" stroke-width="1.6"><rect x="1" y="3" width="10" height="10"/><path d="M3 7l3 3 7-9"/></svg>Help desk services</li>
      </ul>
    </div>
  </div>
</section>

</body>
</html>
```